Bright Harbor Dental*

Promotion for a new dental office
brightharbrdntl.example

I just opened a new dental office and would like to promote my office to
the public. I attached some examples. I have AI files for logo and also can
provide office pictures. Website is brightharbordntl.example.

Target Market(s)

General public

Requirements
Must have
• Dr. Olund
• Kessler State U, BS, MCB
• Marrow Vale School of Dentistry
• Grenfield Guard Veteran
• New patient exam, X-rays and basic cleaning for $95.
• White background
• 20% discount with this post card. This only applied to private pay patients(in fine print)
• Open saturdays and evenings
Should not have
• No postal info. Not going to mail this out.

```html
<!DOCTYPE html>
<html lang="en">
<head>
<meta charset="utf-8">
<title>Bright Harbor Dental – Postcard</title>
<link rel="stylesheet" href="https://fonts.googleapis.com/css2?family=Cinzel:wght@400;600&family=Open+Sans:ital,wght@0,400;0,600;0,700;1,700&display=swap">
<style>
  :root{
    --page:#ffffff;
    --teal:#2b8aa3;
    --teal-deep:#237a92;
    --slate:#4a4647;
    --white:#ffffff;
    --ink:#333132;
    --photo-warm:#c9a68a;
    --map:#e4e6e2;
  }
  *{box-sizing:border-box;margin:0;padding:0}
  html,body{width:1200px;height:1200px;overflow:hidden;background:var(--page);font-family:"Open Sans",Arial,sans-serif;color:var(--white)}
  .card{position:absolute;overflow:hidden;background:var(--white);box-shadow:0 2px 10px rgba(0,0,0,.22)}
  .abs{position:absolute}

  /* FRONT */
  .front{left:92px;top:58px;width:678px;height:526px;background:var(--teal)}
  .front .hero-photo{left:0;top:0;width:350px;height:526px;background:linear-gradient(160deg,#9a9ca3 0%,#b48a6a 45%,var(--photo-warm) 70%,#efe9e4 100%)}
  .front .divider{left:0;top:0;width:678px;height:526px}
  .logo-mark{border:1.5px solid var(--white);border-radius:50%}
  .front .logo-mark{left:378px;top:28px;width:54px;height:54px}
  .front .brand-name{left:440px;top:40px;font-size:18px;font-weight:400;letter-spacing:.6px;white-space:nowrap}
  .front .brand-tag{left:442px;top:66px;font-size:12px;letter-spacing:.3px;white-space:nowrap}
  .headline-top{left:340px;width:338px;top:100px;text-align:center;font-family:"Cinzel",serif;font-size:20px;letter-spacing:.5px}
  .headline-main{left:340px;width:338px;top:116px;text-align:center;font-family:"Cinzel",serif;font-weight:600;font-size:39px;letter-spacing:1px}
  .services-title{left:380px;width:260px;top:174px;display:flex;align-items:center;gap:10px;font-family:"Cinzel",serif;font-size:24px}
  .services-title::before,.services-title::after{content:"";flex:1;height:1.5px;background:var(--white)}
  .service-list{left:356px;top:212px;width:312px;display:grid;grid-template-columns:158px 150px;row-gap:8px;font-size:14px}
  .service-list li{list-style:none;display:flex;align-items:center;gap:5px;white-space:nowrap}
  .service-list svg{width:14px;height:14px;flex:none}
  .front .intro{left:357px;top:277px;width:302px;font-size:10.6px;line-height:14.3px;text-align:justify}
  .front .doctor-box{left:354px;top:348px;width:291px;height:74px;border:1.5px solid var(--white);padding:3px 0 0 16px}
  .doctor-name{font-weight:700;font-style:italic;font-size:17px;line-height:22px}
  .front .doctor-box p{font-size:10.5px;line-height:14.5px}
  .offer{border:1.5px dotted var(--white);border-radius:8px;display:flex;align-items:center;justify-content:center;white-space:nowrap}
  .front .offer{left:339px;top:438px;width:320px;height:34px;font-size:12.5px}
  .front .web-band{left:330px;top:482px;width:348px;height:44px;background:var(--slate);display:flex;align-items:center;justify-content:center;font-size:16px;letter-spacing:1.6px}
  .ribbon{height:38px;display:flex;align-items:center;font-size:12px;letter-spacing:.4px;white-space:nowrap}
  .ribbon-teal{left:0;top:430px;width:230px;background:var(--teal);padding-left:18px;clip-path:polygon(0 0,96% 0,100% 100%,0 100%)}
  .ribbon-slate{left:60px;top:470px;width:270px;background:var(--slate);padding-left:18px;clip-path:polygon(5% 0,100% 0,100% 100%,0 100%)}

  /* BACK */
  .back{left:426px;top:622px;width:691px;height:533px}
  .back .teal-panel{left:0;top:0;width:691px;height:533px}
  .snapshot{border:4px solid var(--white);box-shadow:0 2px 4px rgba(0,0,0,.25)}
  .snap-a{left:22px;top:24px;width:150px;height:118px;transform:rotate(-4deg);background:linear-gradient(135deg,#dfe6ec,#6f8fb8 60%,#3c5d99)}
  .snap-b{left:184px;top:34px;width:152px;height:118px;transform:rotate(-4deg);background:linear-gradient(135deg,#b9c2c9,#d8b9a4 45%,#3a5aa0 80%)}
  .back .intro{left:23px;top:172px;width:328px;font-size:11.2px;font-weight:700;line-height:14.5px;text-align:justify}
  .back .doctor-band{left:0;top:238px;width:380px;height:75px;background:var(--slate);padding:4px 0 0 23px}
  .back .doctor-band p{font-size:12.5px;line-height:16.5px}
  .back .offer{left:17px;top:326px;width:349px;height:34px;font-size:13.5px}
  .offer strong{font-weight:700;font-size:1.1em;margin-left:3px}
  .map-area{left:24px;top:381px;width:134px;height:136px;border:2px solid var(--slate);background:linear-gradient(135deg,var(--map),#d3dccf)}
  .contact-tab{left:161px;top:382px;width:162px;height:23px;background:var(--slate);clip-path:polygon(0 0,100% 0,93% 100%,0 100%);padding-left:9px;font-weight:700;font-size:14px;line-height:23px}
  .contact-list{left:168px;top:415px;list-style:none;font-size:11.8px;line-height:15px}
  .contact-list li{display:flex;align-items:flex-start;gap:8px;margin-bottom:5px;white-space:nowrap}
  .contact-list svg{width:14px;height:14px;flex:none;margin-top:1px}
  .back .logo-mark{left:400px;top:19px;width:22px;height:22px;border-color:var(--slate)}
  .back .brand-name{left:428px;top:22px;font-size:12px;color:var(--slate);white-space:nowrap}

  .discount{left:405px;top:170px;width:270px;text-align:center;color:var(--ink)}
  .discount-rate{font-size:64px;font-weight:700;line-height:70px;color:var(--teal)}
  .discount-label{font-size:20px;font-weight:700;letter-spacing:1px;color:var(--slate)}
  .discount-note{margin-top:6px;font-size:14px}
  .discount-rule{margin:16px auto 0;width:180px;height:1.5px;background:var(--teal)}
  .fine-print{margin-top:10px;font-size:9.5px;line-height:13px;color:#666}
</style>
</head>
<body>

<section class="card front">
  <div class="abs hero-photo" role="img" aria-label="Portrait photo of a smiling woman with long wavy hair"></div>
  <svg class="abs divider" viewBox="0 0 678 526" aria-hidden="true">
    <path d="M340 0 C352 120 330 300 340 526 L678 526 L678 0 Z" fill="var(--teal)"/>
    <path d="M336 0 L352 0 C362 140 338 330 352 526 L338 526 C322 320 346 150 336 0 Z" fill="var(--slate)"/>
    <path d="M330 0 L336 0 C346 150 322 320 338 526 L330 526 C314 320 340 150 330 0 Z" fill="var(--white)"/>
  </svg>

  <div class="abs logo-mark"></div>
  <div class="abs brand-name">BRIGHT HARBOR DENTAL</div>
  <div class="abs brand-tag">MODERN GENERAL DENTISTRY</div>

  <div class="abs headline-top">PATIENT COMFORT IS OUR</div>
  <div class="abs headline-main">TOP PRIORITY</div>
  <div class="abs services-title">Our Services</div>

  <ul class="abs service-list">
    <li><svg viewBox="0 0 14 14"><rect x="1" y="3" width="10" height="10" fill="none" stroke="#fff" stroke-width="1.4"/><path d="M3 7l3 3 7-9" fill="none" stroke="#fff" stroke-width="2"/></svg>Personalized Care</li>
    <li><svg viewBox="0 0 14 14"><rect x="1" y="3" width="10" height="10" fill="none" stroke="#fff" stroke-width="1.4"/><path d="M3 7l3 3 7-9" fill="none" stroke="#fff" stroke-width="2"/></svg>High Quality Care</li>
    <li><svg viewBox="0 0 14 14"><rect x="1" y="3" width="10" height="10" fill="none" stroke="#fff" stroke-width="1.4"/><path d="M3 7l3 3 7-9" fill="none" stroke="#fff" stroke-width="2"/></svg>Patient Centered</li>
    <li><svg viewBox="0 0 14 14"><rect x="1" y="3" width="10" height="10" fill="none" stroke="#fff" stroke-width="1.4"/><path d="M3 7l3 3 7-9" fill="none" stroke="#fff" stroke-width="2"/></svg>Modern Dentistry</li>
  </ul>

  <p class="abs intro">Welcome to Bright Harbor Dental. We are a new modern full service dental office, located in Harbor Point, eager to serve communities in <strong>the Bay Coast. Dr. Olund</strong> and his staff value and treat each of our patients as our own family member.</p>

  <div class="abs doctor-box">
    <div class="doctor-name">Dr. Arin Olund</div>
    <p>Kessler State U, BS, MCB with emphasis in immunology</p>
    <p>Marrow Vale School of Dentistry</p>
    <p>Grenfield Guard Veteran</p>
  </div>

  <div class="abs offer">New patient exam, X-rays and basic cleaning for <strong>$95</strong>.</div>
  <div class="abs web-band">www.brightharbrdntl.example</div>

  <div class="abs ribbon ribbon-teal">OPEN EVENINGS AND SATURDAYS</div>
  <div class="abs ribbon ribbon-slate">MODERN STATE OF THE ART EQUIPMENT</div>
</section>

<section class="card back">
  <svg class="abs teal-panel" viewBox="0 0 691 533" aria-hidden="true">
    <path d="M0 0 L368 0 C388 160 376 380 370 533 L0 533 Z" fill="var(--teal)"/>
    <path d="M368 0 L384 0 C404 170 396 390 376 533 L370 533 C376 380 388 160 368 0 Z" fill="var(--slate)"/>
  </svg>

  <div class="abs snapshot snap-a" role="img" aria-label="Photo of a young patient in a dental chair viewing an X-ray on a tablet"></div>
  <div class="abs snapshot snap-b" role="img" aria-label="Photo of a smiling dental technician at work in the lab"></div>

  <p class="abs intro">We strive to meet your specific dental needs. Your trust is important to us, and we never push unnecessary procedures. We maintain a high standard of excellence in all aspects of dental practice.</p>

  <div class="abs doctor-band">
    <div class="doctor-name">Dr. Arin Olund</div>
    <p>Kessler State U, BS, MCB with emphasis in immunology</p>
    <p>Marrow Vale School of Dentistry</p>
    <p>Grenfield Guard Veteran</p>
  </div>

  <div class="abs offer">New patient exam, X-rays and basic cleaning for <strong>$95</strong>.</div>

  <div class="abs map-area" role="img" aria-label="Street map showing the office location"></div>
  <div class="abs contact-tab">Contact us Today !</div>
  <ul class="abs contact-list">
    <li><svg viewBox="0 0 14 14"><path d="M7 1a4.5 4.5 0 0 0-4.5 4.5C2.5 9 7 13.5 7 13.5S11.5 9 11.5 5.5A4.5 4.5 0 0 0 7 1z" fill="#fff"/><circle cx="7" cy="5.5" r="1.7" fill="var(--teal)"/></svg><span>415 Lantern Rd.<br>Harbor Point, ST 00000</span></li>
    <li><svg viewBox="0 0 14 14"><circle cx="7" cy="7" r="6.2" fill="none" stroke="#fff" stroke-width="1.2"/><path d="M4.5 4c.5 2.8 2.6 5 5.3 5.6l.9-1.3-1.5-.9-.7.6C7.4 7.5 6.6 6.7 6.1 5.6l.6-.7-.8-1.6z" fill="#fff"/></svg><span>555-014-2270</span></li>
    <li><svg viewBox="0 0 14 14"><rect x="1" y="3" width="12" height="8" fill="#fff"/><path d="M1 3l6 5 6-5" fill="none" stroke="var(--teal)" stroke-width="1.2"/></svg><span>hi@brightharbordntl.example</span></li>
    <li><svg viewBox="0 0 14 14"><circle cx="7" cy="7" r="6" fill="none" stroke="#fff" stroke-width="1.2"/><ellipse cx="7" cy="7" rx="2.6" ry="6" fill="none" stroke="#fff" stroke-width="1"/><path d="M1 7h12M2 4h10M2 10h10" stroke="#fff" stroke-width="1"/></svg><span>www.brightharbordntl.example</span></li>
  </ul>

  <div class="abs logo-mark"></div>
  <div class="abs brand-name">BRIGHT HARBOR DENTAL</div>

  <div class="abs discount">
    <div class="discount-rate">20%</div>
    <div class="discount-label">DISCOUNT</div>
    <p class="discount-note">with this post card</p>
    <div class="discount-rule"></div>
    <p class="fine-print">This discount only applies to private pay patients.</p>
  </div>
</section>

</body>
</html>
```